Business Card - connecting 2 souls and beggining the journey of self discovery

Logo on the front
with tag line

On the back list of services and contact details

Seminars
workshops
Coaching
podcasts

Daniel Porthwick
Health & Wellbeing Life Coach
0491 372 815
daniel@wovenpathwellness.example
wovenpathwellness.example

Industry/Entity Type

Life Coaching

Contact Information for Business Card

I like the use of colour from the logo to be used. I'm not a fan of white.

Requirements
Must have
• My tagline: Every good path begins within you
Nice to have
• Use of colour that is in the mind body soul logo

```html
<!DOCTYPE html>
<html lang="en">
<head>
<meta charset="utf-8">
<title>Woven Path Wellness — Business Card</title>
<link rel="stylesheet" href="https://fonts.googleapis.com/css2?family=Arimo:wght@400;700&family=Questrial&display=swap">
<style>
  :root {
    --stage: #e7e4df;
    --card: #ffffff;
    --card-front-top: #f4f4f4;
    --card-front-bottom: #dedede;
    --purple: #7e47a0;
    --teal: #3fa084;
    --ink-grey: #6e6e6e;
    --ink-soft: #8a8a8a;
    --brand-grey: #707070;
  }
  * { box-sizing: border-box; margin: 0; padding: 0; }
  html, body { width: 1200px; height: 1023px; overflow: hidden; }
  body {
    background: var(--stage);
    font-family: "Arimo", Arial, sans-serif;
    position: relative;
  }
  .card {
    position: absolute;
    left: 220px;
    width: 760px;
    height: 434px;
    border-radius: 3px;
    box-shadow: 0 6px 18px rgba(0,0,0,.18);
    overflow: hidden;
  }
  /* Details side */
  .card--details { top: 52px; background: var(--card); }
  .card__bands { position: absolute; inset: 0; }
  .brand-lockup {
    position: absolute; left: 52px; top: 150px;
    display: flex; flex-direction: column; align-items: flex-start; gap: 16px;
  }
  .brand-mark {
    width: 70px; height: 70px; border-radius: 50%;
    background: var(--teal); margin-left: 14px;
  }
  .brand-name {
    font-family: "Questrial", Arial, sans-serif;
    font-size: 28px; color: var(--brand-grey); letter-spacing: -0.5px;
    white-space: nowrap;
  }
  .person {
    position: absolute; right: 48px; top: 72px; text-align: right;
  }
  .person__name { font-size: 30px; font-weight: 700; color: var(--purple); }
  .person__role { font-size: 17px; color: var(--ink-soft); margin-top: 6px; }
  .contact {
    position: absolute; right: 48px; top: 168px;
    list-style: none; text-align: right;
  }
  .contact li {
    display: flex; justify-content: flex-end; align-items: center; gap: 10px;
    font-size: 16px; color: var(--ink-grey); line-height: 26px;
  }
  .contact svg { width: 15px; height: 15px; flex: none; }
  .services {
    position: absolute; right: 48px; top: 296px;
    font-size: 17px; color: var(--ink-soft); letter-spacing: .3px;
  }
  /* Tagline side */
  .card--tagline {
    top: 538px;
    background: linear-gradient(160deg, var(--card-front-top), var(--card-front-bottom));
  }
  .front-brand {
    position: absolute; left: 70px; top: 150px;
  }
  .front-brand__name {
    font-family: "Questrial", Arial, sans-serif;
    font-weight: 400;
    font-size: 48px; color: var(--brand-grey); letter-spacing: -1px;
    white-space: nowrap;
  }
  .front-brand__tagline {
    font-size: 18px; color: var(--ink-grey); font-style: italic; margin-top: 16px;
  }
  .front-mark {
    position: absolute; right: 64px; top: 147px;
    width: 140px; height: 140px; border-radius: 50%;
    background: var(--teal);
  }
</style>
</head>
<body>

<section class="card card--details" aria-label="Business card, contact side">
  <svg class="card__bands" viewBox="0 0 760 434" aria-hidden="true">
    <polygon points="612,0 672,0 642,20" fill="var(--purple)"/>
    <polygon points="652,0 700,0 680,14" fill="var(--teal)"/>
    <polygon points="0,356 360,356 392,384 760,384 760,396 0,396" fill="var(--purple)"/>
    <rect x="0" y="400" width="760" height="34" fill="var(--teal)"/>
  </svg>

  <div class="brand-lockup">
    <span class="brand-mark"></span>
    <span class="brand-name">Woven Path Wellness</span>
  </div>

  <div class="person">
    <p class="person__name">Daniel Porthwick</p>
    <p class="person__role">Health &amp; Wellbeing Life Coach</p>
  </div>

  <ul class="contact">
    <li>0491 372 815
      <svg viewBox="0 0 16 16"><path d="M4 1.5l2.3 3-1.3 1.6c.8 1.8 2.2 3.2 4 4l1.6-1.3 3 2.3-1.3 2.4C7.4 13.3 2.7 8.6 1.5 3.7z" fill="var(--purple)"/></svg>
    </li>
    <li>daniel@wovenpathwellness.example
      <svg viewBox="0 0 16 16"><rect x="1" y="3" width="14" height="10" rx="1" fill="var(--purple)"/><path d="M1.5 3.8L8 9l6.5-5.2" stroke="#fff" stroke-width="1.2" fill="none"/></svg>
    </li>
    <li>www.wovenpathwellness.example
      <svg viewBox="0 0 16 16"><circle cx="8" cy="8" r="6.5" fill="var(--purple)"/><path d="M1.5 8h13M8 1.5c-3 3.5-3 9.5 0 13M8 1.5c3 3.5 3 9.5 0 13M2.8 4.6h10.4M2.8 11.4h10.4" stroke="#fff" stroke-width=".9" fill="none"/></svg>
    </li>
  </ul>

  <p class="services">Seminars | Workshops | Coaching | Podcasts</p>
</section>

<section class="card card--tagline" aria-label="Business card, brand side">
  <div class="front-brand">
    <h1 class="front-brand__name">Woven Path Wellness</h1>
    <p class="front-brand__tagline">Every good path begins within you</p>
  </div>
  <span class="front-mark"></span>
</section>

</body>
</html>
```